Lowell Brandt

20 Year Licensed Master Barber specializing in:
men/women cuts, Grooming, Straight razor Shaving and tape line enhancement, beard grooming, eye brow enhancement, South of France, Hot Towel Treatments, Scalp, Blow outs, Shags, Custom Design,RazorCuts,Shear Cuts, Bobs, Perms, Relaxers, Shoe Shine.
Please create a wonderful business card incorporating all the info above and selecting one of the photos. Please be creative.

Barber

```html
<!DOCTYPE html>
<html lang="en">
<head>
<meta charset="utf-8">
<title>Lowell Brandt – Master Barber Business Card</title>
<link href="https://fonts.googleapis.com/css2?family=Arimo:wght@400;700&display=swap" rel="stylesheet">
<style>
  :root {
    --backdrop: #3b3230;
    --card: #111114;
    --card-edge: #1c1c21;
    --text: #e9e9ee;
    --muted: #c9c9d2;
    --accent: #3c3cc4;
    --seal: #f4f4f7;
    --seal-ring: #2f2f9c;
    --divider: #8a8a94;
  }
  * { box-sizing: border-box; margin: 0; padding: 0; }
  html, body { width: 1200px; height: 864px; overflow: hidden; }
  body {
    background: var(--backdrop);
    font-family: "Arimo", Arial, sans-serif;
    position: relative;
  }
  .card {
    position: absolute;
    width: 540px;
    height: 309px;
    background: var(--card);
    border: 1px solid var(--card-edge);
    border-radius: 4px;
    box-shadow: 0 18px 40px rgba(0,0,0,.5);
    overflow: hidden;
  }
  .card--front { left: 40px; top: 200px; }
  .card--back { left: 620px; top: 355px; }

  /* front */
  .brand-seal {
    position: absolute;
    display: flex; align-items: center; justify-content: center;
    border-radius: 50%;
    text-align: center;
    font-weight: 700;
    line-height: 1.05;
    z-index: 2;
  }
  .card--front .brand-seal {
    left: 24px; top: 20px; width: 78px; height: 78px;
    border: 2px solid var(--muted);
    color: var(--muted);
    font-size: 12px;
  }
  .services {
    position: absolute; left: 24px; top: 114px; width: 222px;
    color: var(--text); font-size: 12px; line-height: 1.38;
    z-index: 2;
  }
  .services strong { font-weight: 700; }
  .portrait {
    position: absolute; right: 0; top: 0; width: 272px; height: 309px;
    z-index: 1;
    background: radial-gradient(ellipse at 50% 55%, #5b5651 0%, #34312f 38%, #151518 72%);
  }

  /* back */
  .card--back .brand-seal {
    left: 48px; top: 78px; width: 150px; height: 150px;
    background: var(--seal);
    border: 6px solid var(--seal-ring);
    color: var(--seal-ring);
    font-size: 21px;
  }
  .divider {
    position: absolute; left: 240px; top: 60px; width: 1px; height: 190px;
    background: linear-gradient(to bottom, transparent, var(--divider), transparent);
  }
  .contact { position: absolute; left: 268px; top: 96px; width: 260px; }
  .contact__name {
    color: var(--accent); font-size: 21px; font-weight: 400; margin-bottom: 14px;
    white-space: nowrap;
  }
  .contact__list { list-style: none; }
  .contact__item {
    display: flex; align-items: center; gap: 9px;
    color: var(--text); font-size: 15px; line-height: 24px;
    white-space: nowrap;
  }
  .contact__icon { width: 14px; height: 14px; flex: none; fill: var(--muted); }
</style>
</head>
<body>
  <section class="card card--front">
    <div class="brand-seal">Lowell<br>Brandt</div>
    <p class="services"><strong>20 Year Licensed Master Barber specializing in</strong> men/women cuts, Grooming, Straight razor Shaving and tape line enhancement, beard grooming, eye brow enhancement, South of France, Hot Towel Treatments, Scalp, Blow outs, Shags, Custom Design, RazorCuts, Shear Cuts, Bobs, Perms, Relaxers, Shoe Shine.</p>
    <div class="portrait" role="img" aria-label="Portrait photo of the barber in a hat and grey jacket"></div>
  </section>

  <section class="card card--back">
    <div class="brand-seal">Lowell<br>Brandt</div>
    <div class="divider"></div>
    <div class="contact">
      <h1 class="contact__name">Lowell Brandt</h1>
      <ul class="contact__list">
        <li class="contact__item">
          <svg class="contact__icon" viewBox="0 0 16 16"><path d="M3 1h3l1.5 4-2 1.3a9 9 0 0 0 4.2 4.2L11 8.5l4 1.5v3a2 2 0 0 1-2 2A12 12 0 0 1 1 3a2 2 0 0 1 2-2z"/></svg>
          (555)318-2046
        </li>
        <li class="contact__item">
          <svg class="contact__icon" viewBox="0 0 16 16"><path d="M1 3h14v10H1z M1 3l7 6 7-6" fill="none" stroke="#c9c9d2" stroke-width="1.6"/></svg>
          lowell.brandt3@example.com
        </li>
        <li class="contact__item">
          <svg class="contact__icon" viewBox="0 0 16 16"><rect x="1" y="1" width="14" height="14" rx="3"/></svg>
          3dbrandt
        </li>
        <li class="contact__item">
          <svg class="contact__icon" viewBox="0 0 16 16"><rect x="1" y="1" width="14" height="14" rx="2"/></svg>
          Lowell.brandt3
        </li>
      </ul>
    </div>
  </section>
</body>
</html>
```